ashby paving works

Needs to have phone number 0412885107 and email marklowry@pavemail.com.au.
ABN 27613048852
name mark lowry

For all your concreting solutions
Excavation
Exposed & colour concrete
House & shed slabs
Driveways
Landing & steps

Contact Information for Business Card

ph 0412885107
email marklowry@pavemail.com.au.
ABN 27613048852
name mark lowry

```html
<!DOCTYPE html>
<html lang="en">
<head>
<meta charset="UTF-8">
<title>Ashby Paving Works – Business Card</title>
<link rel="stylesheet" href="https://fonts.googleapis.com/css2?family=Montserrat:wght@400;500;700&display=swap">
<style>
  :root {
    --orange: #f06a22;
    --grey: #666666;
    --white: #ffffff;
    --backdrop: #2b2b2b;
    --text-dark: #555555;
  }
  * { box-sizing: border-box; margin: 0; padding: 0; }
  html, body { width: 1200px; height: 1200px; overflow: hidden; }
  body {
    background: var(--backdrop);
    font-family: "Montserrat", Arial, sans-serif;
    position: relative;
  }
  .card {
    position: absolute;
    left: 150px;
    width: 900px;
    height: 500px;
    overflow: hidden;
  }

  /* Back side */
  .card-back { top: 60px; background: var(--orange); color: var(--white); }
  .card-back .grey-wedge { position: absolute; inset: 0; }
  .tagline {
    position: absolute; left: 44px; top: 62px;
    font-size: 34px; font-weight: 700; letter-spacing: 1px;
  }
  .tagline-rule {
    position: absolute; left: 0; top: 116px; width: 792px; height: 3px;
    background: var(--grey);
  }
  .services {
    position: absolute; left: 44px; top: 150px;
    list-style: none; font-size: 30px; font-weight: 500; line-height: 42px; letter-spacing: 1px;
  }
  .services li { position: relative; padding-left: 38px; }
  .services li::before {
    content: ""; position: absolute; left: 0; top: 15px;
    width: 14px; height: 14px; background: var(--white);
  }
  .contact-phone {
    position: absolute; left: 600px; top: 270px; width: 280px; text-align: center;
  }
  .contact-phone svg { display: block; margin: 0 auto 14px; }
  .contact-phone .number { font-size: 32px; font-weight: 500; letter-spacing: 4px; }

  /* Front side */
  .card-front { top: 640px; background: var(--white); }
  .front-band {
    position: absolute; left: 0; right: 0; top: 300px; bottom: 0; background: var(--orange);
  }
  .brand-mark {
    position: absolute; left: 80px; top: 100px; width: 100px; height: 100px; background: var(--orange);
  }
  .brand-divider {
    position: absolute; left: 226px; top: 50px; width: 3px; height: 220px; background: var(--orange);
  }
  .brand-block { position: absolute; left: 258px; top: 92px; }
  .brand-name {
    font-size: 40px; font-weight: 700; color: var(--orange); letter-spacing: 1px;
  }
  .brand-rule { width: 560px; height: 3px; background: var(--grey); margin: 10px 0 12px; }
  .brand-phone {
    font-size: 30px; font-weight: 500; color: var(--orange); letter-spacing: 4px;
  }
  .owner-details {
    position: absolute; left: 440px; top: 322px; color: var(--white); width: 440px;
  }
  .owner-name { font-size: 36px; font-weight: 500; letter-spacing: 1px; }
  .owner-rule { height: 2px; background: var(--white); margin: 8px 0 10px; }
  .owner-line { font-size: 22px; font-weight: 500; letter-spacing: 1px; }
</style>
</head>
<body>

<section class="card card-back">
  <svg class="grey-wedge" width="900" height="500" viewBox="0 0 900 500" aria-hidden="true">
    <polygon points="900,0 900,500 440,500" fill="var(--grey)"/>
  </svg>
  <h2 class="tagline">For all your concreting solutions</h2>
  <div class="tagline-rule"></div>
  <ul class="services">
    <li>Excavation</li>
    <li>Exposed &amp; colour concrete</li>
    <li>House &amp; shed slabs</li>
    <li>Driveways</li>
    <li>Landing &amp; steps</li>
  </ul>
  <div class="contact-phone">
    <svg width="260" height="64" viewBox="0 0 260 64" aria-hidden="true">
      <line x1="10" y1="32" x2="90" y2="32" stroke="#fff" stroke-width="3"/>
      <line x1="170" y1="32" x2="250" y2="32" stroke="#fff" stroke-width="3"/>
      <circle cx="130" cy="32" r="28" fill="none" stroke="#fff" stroke-width="4"/>
      <path d="M119 19c3-2 5 0 6 3l2 5c1 2 0 3-2 4l-2 1c1 5 5 9 10 11l1-2c1-2 3-3 5-2l5 2c3 1 4 3 2 6c-2 3-5 4-8 3c-11-3-19-11-22-22c-1-4 1-7 3-9z" fill="#fff"/>
    </svg>
    <p class="number">0412885107</p>
  </div>
</section>

<section class="card card-front">
  <div class="front-band"></div>
  <div class="brand-mark"></div>
  <div class="brand-divider"></div>
  <div class="brand-block">
    <h1 class="brand-name">ASHBY PAVING WORKS</h1>
    <div class="brand-rule"></div>
    <p class="brand-phone">0412885107</p>
  </div>
  <div class="owner-details">
    <p class="owner-name">Mark Lowry</p>
    <div class="owner-rule"></div>
    <p class="owner-line">marklowry@pavemail.com.au</p>
    <div class="owner-rule"></div>
    <p class="owner-line">ABN 27613048852</p>
  </div>
</section>

</body>
</html>
```